Australian HR Consultancy Company Brochure (and more!). Our tagline "Start something amazing."

We are a start-up HR and Recruitment consultancy. We have a group of young, passionate and top performing staff who assist companies with driving their workforce productivity, keeping employees happy, hiring fantastic people and ensuring legal compliance across the HR field.

We work across a variety of sectors such as mining, Not for Profits, Finance, Accounting, Health etc so are not pigeon-holed to one particular group. We tend to deal with medium sized businesses.

Our team is professional and corporate but down to earth and approachable. We have unique offerings in terms of our services and our pricing. We deliver exceptional value to our clients and build long term mutually beneficial relationships. We care about giving back to the community and doing the right thing by everyone we deal with.

Our design should communicate that we are corporate and professional but not uptight 'suits', that we are fresh and engaging. Clear, concise, crisp but not cold.

Thinking 6 page brochure.

We have a variety of colours in our logo and tend to lean towards fresh shades of blue and green but are definitely open to other colours such as purple, pink, orange etc. We would prefer the brochure to be in landscape format (like a powerpoint presentation) as apparently that's easier to read? but open to your expert suggestions!

Target Market(s)

Medium sized business across all industries but within the professional area ie finance, mining, health.

Industry/Entity Type

It Company

Colors
33b8a4
33a6d7
0592cd
85cae6
86cfc6
b768aa

Requirements
Must have
• Needs to be editable version as we will be changing our tagline and about us in the new year.

```html
<!DOCTYPE html>
<html lang="en">
<head>
<meta charset="utf-8">
<title>TeamSpring Brochure Spreads</title>
<link href="https://fonts.googleapis.com/css2?family=Heebo:wght@300;400;500;700&display=swap" rel="stylesheet">
<style>
:root{
  --slate:#324455;
  --cyan:#12a9dc;
  --cyan-text:#1aa6d8;
  --white:#ffffff;
  --ink:#2c3a47;
  --paper:#ffffff;
}
*{margin:0;padding:0;box-sizing:border-box}
html,body{width:1200px;height:973px;overflow:hidden;background:var(--paper)}
body{position:relative;font-family:'Heebo',sans-serif;color:var(--ink)}
.page{position:absolute;overflow:hidden}
.abs{position:absolute}
.photo{position:absolute}
/* cover spread */
.cover{left:31px;top:43px;width:571px;height:405px;background:var(--white)}
.cover .photo{left:0;top:0;width:571px;height:335px;background:linear-gradient(135deg,#f4f6f7 0%,#e3e7ea 45%,#a9a39c 75%,#5a4e47 100%)}
.headline{left:47px;top:24px;font-weight:300;font-size:40px;line-height:36px;color:var(--cyan-text)}
.cover-tag{left:46px;top:350px;font-weight:300;font-size:13.5px;line-height:16.5px;color:var(--ink)}
.brand{display:flex;align-items:center;gap:7px;font-weight:500;font-size:23px;line-height:26px;color:var(--ink);letter-spacing:-0.3px;white-space:nowrap}
.brand .dot{width:24px;height:24px;border-radius:50%;background:var(--cyan);flex:none}
.cover .brand{left:364px;top:358px}
.back{left:602px;top:43px;width:571px;height:405px;background:var(--white)}
.back .panel{position:absolute;left:0;top:0;width:571px;height:335px;background:var(--slate)}
.contact{left:0;top:192px;width:571px;text-align:center;color:var(--white);font-size:13.5px;line-height:19px}
.contact .lead{font-weight:300}
.contact strong{font-weight:700}
.back .brand{left:364px;top:358px}
/* inner spread */
.inner-left{left:26px;top:526px;width:570px;height:402px;background:var(--slate);color:var(--white)}
.inner-right{left:596px;top:526px;width:567px;height:402px;background:var(--white)}
.about-title{left:71px;top:36px;font-weight:300;font-size:20px;line-height:22px;color:var(--white)}
.about-copy{left:71px;top:62px;width:148px;font-size:6px;line-height:7.3px;font-weight:300}
.about-copy b{font-weight:700}
.about-photo{left:71px;top:146px;width:143px;height:97px;background:linear-gradient(120deg,#e8e2d8,#c9b7a2 55%,#7e6a5b)}
.quote{left:62px;top:262px;width:165px;font-weight:300;font-size:14px;line-height:16.5px}
.quote .mark{color:var(--cyan);font-weight:500}
.card{position:absolute;width:240px;overflow:hidden}
.card .photo{left:0;top:0;width:240px;height:157px}
.workshops{left:274px;top:38px;height:311px;background:var(--cyan)}
.workshops .photo{background:linear-gradient(135deg,#dfe8ef,#6f8aa3 55%,#2d3e52)}
.card-body{position:absolute;left:17px;top:168px;right:12px}
.card-title{font-weight:300;font-size:19px;line-height:22px;white-space:nowrap}
.workshops .card-title{color:var(--slate)}
.card-lead{font-size:10px;line-height:11.5px;margin-top:3px;font-weight:400}
.card-small{font-size:6px;line-height:7.5px;font-weight:300;margin-top:6px}
.cols{display:grid;grid-template-columns:1fr 1fr;margin-top:7px}
ul.list{list-style:none}
ul.list li{position:relative;padding-left:13px;font-size:6.3px;line-height:10.7px;font-weight:300;white-space:nowrap}
ul.list li::before{content:"";position:absolute;left:2px;top:4.5px;width:2.5px;height:2.5px;border-radius:50%;background:currentColor}
.workshops ul.list li{color:var(--white);line-height:10.5px}
.workshops .card-lead,.workshops .card-small{color:var(--white)}
.service{left:69px;width:205px}
.service h2{font-weight:300;font-size:19px;line-height:22px;color:var(--cyan-text)}
.service .card-lead{color:var(--ink);margin:3px 0 6px;font-size:9.6px;line-height:11px;letter-spacing:-0.15px;white-space:nowrap}
.strategic{top:36px}
.foundations{top:198px}
.placements{left:289px;top:39px;height:310px;background:var(--slate);color:var(--white)}
.placements .photo{background:linear-gradient(160deg,#d9dee3,#a8a7ab 45%,#8a5b55 75%,#3b3a40)}
.placements .card-body{top:170px;left:15px;right:10px}
.placements .card-title{color:var(--cyan-text);font-size:18.5px}
.placements .card-lead{color:var(--white);margin-bottom:8px}
.placements ul.list li{line-height:10.6px}
</style>
</head>
<body>

<section class="page cover">
  <div class="photo" role="img" aria-label="Presenter speaking to a seated group in a bright training room"></div>
  <h1 class="abs headline">Start<br>something<br>amazing.</h1>
  <p class="abs cover-tag">We help organisations reach their full<br>potential through the power of their people.</p>
  <div class="abs brand"><span class="dot"></span>TeamSpring</div>
</section>

<section class="page back">
  <div class="panel"></div>
  <div class="abs contact">
    <div class="lead">Start a conversation with us</div>
    <strong>www.teamspring.com.au</strong><br>
    <strong>Phone: 1300 555 010</strong>
  </div>
  <div class="abs brand"><span class="dot"></span>TeamSpring</div>
</section>

<section class="page inner-left">
  <h2 class="abs about-title">About Us</h2>
  <p class="abs about-copy"><b>TeamSpring</b> is a fresh, innovative leader in the provision of human resources, workplace relations and recruitment services. Our tailored approach helps us meet the needs and goals of a varied group of growing Australian businesses.<br>We are committed to delivering outstanding service and value that ensures the best results for our long-term business partners.</p>
  <div class="abs about-photo" role="img" aria-label="Two colleagues reviewing work together at a desk"></div>
  <p class="abs quote"><span class="mark">&ldquo;</span>We help organisations reach their full potential through the power of their people.<span class="mark">&rdquo;</span></p>

  <div class="card workshops">
    <div class="photo" role="img" aria-label="Two businessmen discussing a tablet"></div>
    <div class="card-body">
      <h2 class="card-title">Workshops</h2>
      <p class="card-lead">Let's start developing your team.</p>
      <p class="card-small">Tailored programs built to make a lasting impact on your organisation and its leaders.</p>
      <p class="card-small">Offered as 1-1.5 hour 'Lunch N Learns', half day or full day sessions as requested across:</p>
      <div class="cols">
        <ul class="list"><li>Leadership Development</li><li>Team Building</li><li>Change Management</li></ul>
        <ul class="list"><li>Culture Building</li><li>Management Basics</li></ul>
      </div>
    </div>
  </div>
</section>

<section class="page inner-right">
  <div class="abs service strategic">
    <h2>Strategic HR</h2>
    <p class="card-lead">Driving organisational success<br>through strategic people design.</p>
    <ul class="list">
      <li>Leadership Development</li><li>Organisational Design</li><li>Change Management</li><li>Culture Programs</li><li>Organisational Capabilities</li><li>Executive &amp; Leadership Coaching</li><li>Employee Engagement &amp; Retention</li><li>Talent Attraction &amp; Acquisition</li>
    </ul>
  </div>
  <div class="abs service foundations">
    <h2>HR Foundations</h2>
    <p class="card-lead">HR foundations are building the HR foundations<br>for legal compliance &amp; employee management.</p>
    <ul class="list">
      <li>Employment Contracts &amp; Agreements</li><li>Organisational Structure &amp; Design</li><li>Terminations &amp; FairWork Advice</li><li>Performance Management</li><li>Recruitment &amp; Onboarding</li><li>Remuneration &amp; Benefits</li><li>HR Policies &amp; Procedures</li><li>Workplace Investigations</li>
    </ul>
  </div>

  <div class="card placements">
    <div class="photo" role="img" aria-label="Audience seated in a seminar room facing a screen"></div>
    <div class="card-body">
      <h2 class="card-title">Professional Placements</h2>
      <p class="card-lead">Start hiring incredible people. Matching great<br>organisations to great people.</p>
      <ul class="list">
        <li>Executive Search</li><li>Recruitment Processing Outsourcing (RPO)</li><li>Contingent &amp; Retained Services</li><li>Permanent Recruitment</li><li>Recruitment Admin Support</li><li>Manager Interview Training</li><li>Talent Attraction &amp; Acquisition Programs</li>
      </ul>
    </div>
  </div>
</section>

</body>
</html>
```